Business card design needed

Bright Path Ahead is an online wellness program designed for people dealing with cancer to take control of their lives and Bright path ahead.

Target Market(s)

initially woman aged 35 to 65 years eventaully then men

Industry/Entity Type

Business

Contact Information for Business Card

Marisol Dunkerly
Bright path ahead Coach
Marisol@brightpathahead.com.au
M 0419382716
Skype Marisol.Dunkerly
local number to come
www.brightpathahead.com.au

Requirements
Must have
• Business cards want to have a photo of me on the back this is a head shot. Also a small blurb " Marisol recovered and survived 2 types of cancer. She under went a transformational 12 month journey to overcome cancer naturally . Join her online coaching program to Bright path ahead.

Phone number and email and skype address.
Nice to have
• Looking for something that resembles health EG abstract tree of life, or something resembling health and balance . Like lime green/apple green want modern fresh. Want only 2 colours used on the cards. Need to use the logo and Bright path ahead on website and email signature - Clean and fresh

Also would like Letter head and logo for website and email signature

```html
<!DOCTYPE html>
<html lang="en">
<head>
<meta charset="utf-8">
<title>Bright path ahead — Business Card</title>
<link href="https://fonts.googleapis.com/css2?family=Questrial&display=swap" rel="stylesheet">
<style>
  :root {
    --backdrop: #3a3d42;
    --blue-deep: #0c2283;
    --blue-mid: #1740b8;
    --blue-bright: #1aa9e3;
    --card-light: #f1f1f0;
    --card-grey: #d6d6d4;
    --ink: #2b2b2b;
    --white: #ffffff;
  }
  * { box-sizing: border-box; margin: 0; padding: 0; }
  html, body { width: 1200px; height: 900px; overflow: hidden; }
  body {
    background: var(--backdrop);
    font-family: "Questrial", "Century Gothic", sans-serif;
    position: relative;
  }
  .presentation-title {
    position: absolute; right: 48px; top: 30px;
    color: var(--white); font-size: 50px; font-weight: 400; letter-spacing: -0.5px;
  }

  .card {
    position: absolute; width: 620px; height: 354px; overflow: hidden;
    box-shadow: 0 14px 30px rgba(0,0,0,0.45);
  }

  /* Front */
  .card-front {
    background:
      linear-gradient(125deg, rgba(255,255,255,0) 18%, rgba(120,220,255,0.55) 30%, rgba(255,255,255,0) 46%),
      linear-gradient(135deg, var(--blue-bright) 0%, var(--blue-mid) 45%, var(--blue-deep) 100%);
  }
  .brand-mark {
    position: absolute; left: 48px; top: 118px; width: 240px;
    color: var(--white); font-size: 40px; line-height: 1.02;
  }
  .contact {
    position: absolute; left: 318px; top: 92px; color: var(--white);
  }
  .contact-name { font-size: 19px; }
  .contact-role { font-size: 13px; margin-bottom: 16px; }
  .contact-list { list-style: none; font-size: 15px; line-height: 21px; }
  .contact-list li { display: flex; align-items: center; gap: 7px; white-space: nowrap; }
  .contact-list svg { width: 13px; height: 13px; flex: none; }

  /* Back */
  .card-back {
    background: linear-gradient(100deg, var(--card-light) 0%, #e6e6e4 60%, var(--card-grey) 100%);
  }
  .portrait {
    position: absolute; left: 300px; top: 0; width: 320px; height: 354px; z-index: 1;
    background:
      linear-gradient(180deg, rgba(0,0,0,0) 55%, rgba(46,170,190,0.35) 75%, rgba(250,250,250,0.9) 100%),
      radial-gradient(ellipse at 45% 35%, #e8cdb4 0%, #d9b58e 28%, #e6e5e2 58%, #ecebe8 100%);
  }
  .blurb {
    position: absolute; left: 20px; top: 22px; width: 290px; z-index: 2;
    text-align: right; color: var(--ink); font-size: 15px; line-height: 19px; white-space: nowrap;
  }
  .blurb p + p { margin-top: 17px; }
  .url-band {
    position: absolute; left: 0; right: 0; top: 262px; height: 50px; z-index: 3;
    background: linear-gradient(90deg, var(--blue-deep) 0%, var(--blue-mid) 45%, var(--blue-bright) 100%);
  }
  .url-band span {
    position: absolute; left: 42px; top: 7px; color: var(--white); font-size: 31px; white-space: nowrap;
  }

  /* Thumbnails */
  .thumb {
    position: absolute; width: 620px; height: 354px;
    transform-origin: top left; transform: scale(0.331);
  }
  .thumb .card { position: absolute; left: 0; top: 0; box-shadow: none; }
</style>
</head>
<body>

<h1 class="presentation-title">Bright path ahead</h1>

<section class="card card-front" style="left:90px; top:108px;">
  <div class="brand-mark">Bright Path Ahead</div>
  <div class="contact">
    <div class="contact-name">Marisol Dunkerly</div>
    <div class="contact-role">Bright path ahead Coach</div>
    <ul class="contact-list">
      <li><svg viewBox="0 0 14 14"><rect x="1" y="3" width="12" height="8" fill="#fff"/><path d="M1 3 L7 8 L13 3" stroke="#1740b8" fill="none" stroke-width="1.2"/></svg>Marisol@brightpathahead.com.au</li>
      <li><svg viewBox="0 0 14 14"><rect x="3.5" y="1" width="7" height="12" rx="1.5" fill="#fff"/><rect x="5" y="3" width="4" height="6" fill="#1740b8"/></svg>0419382716</li>
      <li><svg viewBox="0 0 14 14"><circle cx="7" cy="7" r="6.5" fill="#fff"/><path d="M4.5 3.5 L6 3.5 L6.5 5.5 L5.5 6.3 Q6.5 8 7.8 8.6 L8.6 7.6 L10.5 8.2 L10.5 9.7 Q7 10.5 4.5 7 Q3.7 5 4.5 3.5Z" fill="#1740b8"/></svg>4528173096</li>
      <li><svg viewBox="0 0 14 14"><circle cx="7" cy="7" r="6.5" fill="#fff"/></svg>Marisol.Dunkerly</li>
    </ul>
  </div>
</section>

<section class="card card-back" style="left:90px; top:488px;">
  <div class="portrait" role="img" aria-label="Head-and-shoulders portrait photo of the coach, smiling, resting her chin on her hand, wearing a white top and turquoise beads"></div>
  <div class="blurb">
    <p>Marisol recovered and<br>survived 2 types of cancer.</p>
    <p>She under went<br>a transformational 12 month journey<br>to overcome cancer naturally.</p>
    <p>Join her online coaching program<br>to Bright path ahead.</p>
  </div>
  <div class="url-band"><span>www.brightpathahead.com.au</span></div>
</section>

<div class="thumb" style="left:945px; top:110px;">
  <section class="card card-front">
    <div class="brand-mark">Bright Path Ahead</div>
    <div class="contact">
      <div class="contact-name">Marisol Dunkerly</div>
      <div class="contact-role">Bright path ahead Coach</div>
      <ul class="contact-list">
        <li><svg viewBox="0 0 14 14"><rect x="1" y="3" width="12" height="8" fill="#fff"/></svg>Marisol@brightpathahead.com.au</li>
        <li><svg viewBox="0 0 14 14"><rect x="3.5" y="1" width="7" height="12" rx="1.5" fill="#fff"/></svg>0419382716</li>
        <li><svg viewBox="0 0 14 14"><circle cx="7" cy="7" r="6.5" fill="#fff"/></svg>4528173096</li>
        <li><svg viewBox="0 0 14 14"><circle cx="7" cy="7" r="6.5" fill="#fff"/></svg>Marisol.Dunkerly</li>
      </ul>
    </div>
  </section>
</div>

<div class="thumb" style="left:945px; top:242px;">
  <section class="card card-back">
    <div class="portrait" role="img" aria-label="Small portrait photo of the coach"></div>
    <div class="blurb">
      <p>Marisol recovered and<br>survived 2 types of cancer.</p>
      <p>She under went<br>a transformational 12 month journey<br>to overcome cancer naturally.</p>
      <p>Join her online coaching program<br>to Bright path ahead.</p>
    </div>
    <div class="url-band"><span>www.brightpathahead.com.au</span></div>
  </section>
</div>

</body>
</html>
```